independant car dealership needs a new sign

we need to design a new sign for our current car dealership using the our new logo as supplied
Down the track the sign must need to be able to be to change out the word Harlowbank on the logo to such things as (workshop or prestige) as we will eventually add on sections to the business
As well as the logo the sign must have the phone numbers (0472 619 258 and 0386 214 537) As well as (LMCT 7326)
Your are more than welcome to have a play with colours but I would prefure to keep the (K Pellings) still green

Thanks
Derek Pelling

Industry/Entity Type

Car Dealer

Colors

Designer to choose colors to be used in the design.

Requirements
Must have
• must have on sign
• (0472 619 258
• 0386 214 537
• LMCT 7326)

```html
<!DOCTYPE html>
<html lang="en">
<head>
<meta charset="utf-8">
<title>Pellings Autocentre – Sign Concepts</title>
<link rel="stylesheet" href="https://fonts.googleapis.com/css2?family=Orbitron:wght@700;900&family=Michroma&family=Exo+2:wght@600&display=swap">
<style>
  :root {
    --backdrop: #8a8a8a;
    --brand-green: #9bbf2c;
    --ink: #2b2a29;
    --paper: #ffffff;
  }
  html, body {
    margin: 0;
    padding: 0;
    width: 1200px;
    height: 1145px;
    overflow: hidden;
    background: var(--backdrop);
  }
  .sign-board {
    position: absolute;
    left: 136px;
    filter: drop-shadow(0 6px 10px rgba(0,0,0,0.35));
  }
  .sign-board--light { top: 120px; }
  .sign-board--green { top: 605px; }
  .brand-name {
    font-family: "Orbitron", sans-serif;
    font-weight: 900;
  }
  .division, .sub-division {
    font-family: "Orbitron", sans-serif;
    font-weight: 700;
  }
  .licence {
    font-family: "Michroma", sans-serif;
  }
  .phone-numbers {
    font-family: "Exo 2", sans-serif;
    font-weight: 600;
  }
</style>
</head>
<body>

<!-- Light variant -->
<svg class="sign-board sign-board--light" width="928" height="394" viewBox="0 0 928 394" role="img" aria-label="Pellings Autocentre sign, white with green contact band">
  <rect width="928" height="394" fill="var(--paper)"/>
  <rect class="contact-band" y="290" width="928" height="104" fill="var(--brand-green)"/>

  <rect class="brand-square" x="110" y="62" width="146" height="146" fill="var(--brand-green)"/>
  <text class="brand-name" x="332" y="118" font-size="88" fill="var(--brand-green)" textLength="552" lengthAdjust="spacingAndGlyphs">PELLINGS</text>
  <text class="division" x="354" y="172" font-size="50" fill="var(--ink)" textLength="530" lengthAdjust="spacingAndGlyphs">AUTOCENTRE</text>
  <rect class="division-rule" x="358" y="200" width="158" height="3" fill="var(--ink)"/>
  <text class="sub-division" x="538" y="210" font-size="32" fill="var(--brand-green)" textLength="344" lengthAdjust="spacingAndGlyphs">HARLOWBANK</text>

  <rect class="licence-rule" x="0" y="278" width="310" height="4" fill="var(--ink)"/>
  <rect class="licence-rule" x="618" y="278" width="310" height="4" fill="var(--ink)"/>
  <text class="licence" x="324" y="285" font-size="32" fill="var(--ink)" textLength="284" lengthAdjust="spacingAndGlyphs">LMCT 7326</text>

  <g class="phone-icon" transform="translate(36 322)" fill="var(--ink)">
    <path d="M6 2 L14 0 L19 12 L13 16 C16 24 21 29 28 33 L32 27 L44 32 L42 40 C38 44 30 44 20 36 C10 28 3 18 3 10 Z" transform="scale(0.8)"/>
    <path d="M0 38 Q4 34 8 37 T16 36 T24 37" stroke="var(--ink)" stroke-width="1" fill="none"/>
  </g>
  <text class="phone-numbers" x="78" y="362" font-size="58" fill="var(--ink)" textLength="812" lengthAdjust="spacingAndGlyphs">0472 619 258, 0386 214 537</text>
</svg>

<!-- Green variant -->
<svg class="sign-board sign-board--green" width="928" height="418" viewBox="0 0 928 418" role="img" aria-label="Pellings Autocentre sign, all green">
  <rect width="928" height="418" fill="var(--brand-green)"/>

  <rect class="brand-square" x="110" y="60" width="146" height="146" fill="var(--paper)"/>
  <text class="brand-name" x="332" y="120" font-size="88" fill="var(--paper)" textLength="552" lengthAdjust="spacingAndGlyphs">PELLINGS</text>
  <text class="division" x="354" y="175" font-size="50" fill="var(--ink)" textLength="530" lengthAdjust="spacingAndGlyphs">AUTOCENTRE</text>
  <rect class="division-rule" x="358" y="203" width="158" height="3" fill="var(--ink)"/>
  <text class="sub-division" x="538" y="213" font-size="32" fill="var(--paper)" textLength="344" lengthAdjust="spacingAndGlyphs">HARLOWBANK</text>

  <rect class="licence-rule" x="0" y="275" width="310" height="4" fill="var(--paper)"/>
  <rect class="licence-rule" x="618" y="275" width="310" height="4" fill="var(--paper)"/>
  <text class="licence" x="324" y="288" font-size="32" fill="var(--paper)" textLength="284" lengthAdjust="spacingAndGlyphs">LMCT 7326</text>

  <g class="phone-icon" transform="translate(36 326)" fill="var(--ink)">
    <path d="M6 2 L14 0 L19 12 L13 16 C16 24 21 29 28 33 L32 27 L44 32 L42 40 C38 44 30 44 20 36 C10 28 3 18 3 10 Z" transform="scale(0.8)"/>
    <path d="M0 38 Q4 34 8 37 T16 36 T24 37" stroke="var(--ink)" stroke-width="1" fill="none"/>
  </g>
  <text class="phone-numbers" x="78" y="366" font-size="58" fill="var(--ink)" textLength="812" lengthAdjust="spacingAndGlyphs">0472 619 258, 0386 214 537</text>
</svg>

</body>
</html>
```